Charity donation cards

I need a card in an envelope that would be given out to people and they would put their donations along with their details (name and email) and give it back to us (dropped in acrylic boxes at events etc).

The card should be a medium size, bi or tri fold to be able to fit all the information i require.

The Wisteren Fund

The Bright Meadow Centre is dedicated to providing the much needed support to families and children struggling with their differences through a holistic and comprehensive approach that includes detailed evaluations, therapy programs and support services to help unlock the potential in every child.

We are so proud to be able to help empower our society by dedicating our business to the mental, physical and social well being of our younger community and pledging all our net profits to help ensure no child is ever left behind.

Professional services can often be expensive. Our Wisteren Fund helps support families requiring financial aid. We believe every child deserves the opportunity to succeed and no child should be left behind.

How can you help?

Gift the therapies to the children that need it the most. We welcome new sponsors, appreciate your gifts and gratefully accept your contributions as we expand to increase the number of children we can serve.

Name:
Email:
Amount:

We accept cash, checks or credit card payments at The Bright Meadow Centre.

Gift cards should be dropped in the designated acrylic boxes at TBMC or the event.

Please email wisterenfund@tbmc-example.org for more information on the process.
Http://www.tbmc-example.org

Target Market(s)

These cards will be placed in the reception for our clients to donate.

We will also be working with party planners. Some parents don't want people to get them gifts for their kids birthday party so they want to use this instead.

Industry/Entity Type

Charity

Requirements
Must have
• The same feel as our centre Http://www.tbmc-example.org
• our website, email and contact number
Nice to have
• Go to our website and feel free to take ideas and content.
• The design should be clean and simple.
• High light the key words in the text with bold and maybe in green to make it pop out.
Should not have
• Do not use the word donate in any print material. The word should be gift.

```html
<!DOCTYPE html>
<html lang="en">
<head>
<meta charset="utf-8">
<title>The Wisteren Fund – Gift Card Set</title>
<link rel="stylesheet" href="https://fonts.googleapis.com/css2?family=Poiret+One&display=swap">
<style>
  :root{
    --page:#ffffff;
    --ink:#3a3a3a;
    --ink-soft:#555555;
    --frame:#b4b4b4;
    --paper:#ffffff;
    --swoosh:#3d3d3d;
    --green:#8fd13c;
    --accent:#f08a1c;
    --flap:#b9b9b9;
  }
  *{box-sizing:border-box;margin:0;padding:0}
  html,body{width:1200px;height:1000px;overflow:hidden;background:var(--page)}
  body{position:relative;font-family:"Poiret One",sans-serif;color:var(--ink);font-weight:400}

  /* ---------- front cover ---------- */
  .cover{position:absolute;left:55px;top:50px;width:550px;height:420px;
    box-shadow:0 4px 14px rgba(0,0,0,.18);overflow:hidden}
  .cover svg{position:absolute;inset:0}
  .cover-brand{position:absolute;left:80px;top:65px;display:flex;align-items:center;gap:20px}
  .cover-brand .brand-ring{width:150px;height:150px;border-radius:50%;
    border:5px solid var(--accent);flex:none}
  .cover-brand .brand-name{font-size:40px;line-height:1.05;color:#ffffff;width:290px}
  .cover-message{position:absolute;left:44px;right:44px;top:322px;
    font-size:14px;line-height:1.5;text-align:center;color:var(--ink-soft)}

  /* ---------- envelope ---------- */
  .envelope{position:absolute;left:55px;top:510px;width:550px;height:420px;
    box-shadow:0 4px 14px rgba(0,0,0,.18);overflow:hidden;background:var(--paper)}
  .envelope svg{position:absolute;inset:0}

  /* ---------- inside spread ---------- */
  .inside{position:absolute;left:620px;top:110px;width:515px;height:765px;
    background:var(--frame);box-shadow:0 4px 14px rgba(0,0,0,.18)}
  .inside-panel{position:absolute;left:22px;top:35px;width:466px;height:672px;
    background:var(--paper);padding:24px 18px 0 18px;font-size:14.2px;line-height:1.38}
  .inside-fold{position:absolute;left:0;right:0;top:335px;height:40px;
    background:linear-gradient(to bottom,rgba(0,0,0,0),rgba(0,0,0,.08) 50%,rgba(0,0,0,0))}
  .hl{background:var(--green);box-decoration-break:clone;-webkit-box-decoration-break:clone;padding:0 2px}
  .panel-title{text-align:center;margin-bottom:6px;font-size:inherit;font-weight:400}
  .panel-text{text-align:justify;text-indent:42px;margin-bottom:12px}
  .panel-text.closing{text-align:center;text-indent:0;margin-top:14px}
  .gift-form{list-style:none;margin:14px 0 0 52px}
  .gift-form li{display:flex;line-height:1.35}
  .gift-form .label{width:64px;text-align:right}
  .gift-form .colon{margin-left:10px}
  .inside-footer{position:absolute;left:0;right:0;top:714px;text-align:center;
    color:#ffffff;font-size:14px;line-height:1.4}
</style>
</head>
<body>

<section class="cover" aria-label="Card front">
  <svg viewBox="0 0 550 420" width="550" height="420" aria-hidden="true">
    <defs>
      <linearGradient id="coverSky" x1="0" y1="0" x2="0" y2="1">
        <stop offset="0" stop-color="#626262"/>
        <stop offset="0.6" stop-color="#bdbdbd"/>
        <stop offset="1" stop-color="#e6e6e6"/>
      </linearGradient>
    </defs>
    <rect width="550" height="420" fill="url(#coverSky)"/>
    <path d="M0,288 C160,305 330,250 550,188 L550,420 L0,420 Z" fill="#ffffff"/>
    <path d="M0,290 C180,312 380,250 550,300 L550,330 C380,268 190,318 0,298 Z" fill="var(--swoosh)"/>
  </svg>
  <div class="cover-brand">
    <span class="brand-ring"></span>
    <span class="brand-name">The Bright Meadow Centre</span>
  </div>
  <p class="cover-message">Gift the therapies to the children that need it the most. We welcome new sponsors, appreciate your gifts and gratefully accept your contributions as we expand to increase the number of children we can serve.</p>
</section>

<section class="envelope" aria-label="Envelope">
  <svg viewBox="0 0 550 420" width="550" height="420">
    <defs>
      <linearGradient id="handsTones" x1="0" y1="0" x2="1" y2="0">
        <stop offset="0" stop-color="#a6a47a"/>
        <stop offset="0.15" stop-color="#d4a86a"/>
        <stop offset="0.3" stop-color="#b98aa4"/>
        <stop offset="0.42" stop-color="#3f6f9a"/>
        <stop offset="0.55" stop-color="#7d2f3a"/>
        <stop offset="0.68" stop-color="#6e9a7c"/>
        <stop offset="0.8" stop-color="#3a2a22"/>
        <stop offset="1" stop-color="#b8895c"/>
      </linearGradient>
    </defs>
    <g aria-hidden="true" stroke="#eeeeee" stroke-width="1.5" fill="none">
      <path d="M0,420 L275,240 L550,420"/>
      <path d="M0,0 L275,240 L550,0"/>
    </g>
    <rect x="40" y="185" width="490" height="235" rx="16" fill="url(#handsTones)" opacity="0.85"
      role="img" aria-label="Illustration of many raised hands in varied skin tones"/>
    <path d="M0,0 L550,0 L550,50 L300,225 Q275,242 250,225 L0,50 Z" fill="var(--flap)" aria-hidden="true"/>
  </svg>
</section>

<section class="inside" aria-label="Card inside">
  <div class="inside-panel">
    <div class="inside-fold" aria-hidden="true"></div>
    <h1 class="panel-title"><span class="hl">The Wisteren Fund</span></h1>
    <p class="panel-text"><span class="hl">The Bright Meadow Centre is dedicated to providing the much needed support to families and children struggling with their differences through a holistic and comprehensive approach that includes detailed evaluations, therapy programs and support services to help unlock the potential in every child.</span></p>
    <p class="panel-text"><span class="hl">We are so proud to be able to help empower our society by dedicating our business to the mental, physical and social well being of our younger community and pledging all our net profits to help ensure no child is ever left behind.</span></p>
    <p class="panel-text"><span class="hl">Professional services can often be expensive. Our Wisteren Fund helps support families requiring financial aid. We believe every child deserves the opportunity to succeed and no child should be left behind.</span></p>
    <h2 class="panel-title"><span class="hl">How can you help?</span></h2>
    <p class="panel-text"><span class="hl">Gift the therapies to the children that need it the most. We welcome new sponsors, appreciate your gifts and gratefully accept your contributions as we expand to increase the number of children we can serve.</span></p>
    <ul class="gift-form">
      <li><span class="label hl">Name</span><span class="colon">:</span></li>
      <li><span class="label hl">Email</span><span class="colon">:</span></li>
      <li><span class="label hl">Amount</span><span class="colon">:</span></li>
    </ul>
    <p class="panel-text closing"><span class="hl">We accept cash, checks or credit card payments at The Bright Meadow Centre. Gift cards should be dropped in the designated acrylic boxes at TBMC or the event.</span></p>
  </div>
  <p class="inside-footer">Please email wisterenfund@tbmc-example.org for more information on the process.<br>Http://www.tbmc-example.org The Wisteren Fund</p>
</section>

</body>
</html>
```